Fenwell Building Partners Stationary Revamp

We need a full set of new stationary including business cards for our Public Sector Construction company based in the South East of England. We have a new logo (attached) that we want to launch and revamp all of our company literature. We are required to send a lot of correspondence to residents etc so a consistent theme is required across everything. Also attached is our existing templates.

Target Market(s)

We work for Council and government provided housing organisations and NOT private individuals. All of our clients represent government spent money, so we need to look professional and instantly recognisable brand.

Industry/Entity Type

Business

Colors

Designer to choose colors to be used in the design.

Requirements
Must have
• New fresh designs that utilise our new logo. And the letterhead needs to be able to be rolled out onto a word template so that all staff can type straight onto it rather than us having to have it printed first.
Nice to have
• I am looking forward to seeing your best efforts as designers.

```html
<!DOCTYPE html>
<html lang="en">
<head>
<meta charset="utf-8">
<title>Fenwell Building Partners – Stationery</title>
<link rel="stylesheet" href="https://fonts.googleapis.com/css2?family=Open+Sans:wght@400;600;700&display=swap">
<style>
  :root {
    --backdrop: #e2e3e3;
    --paper: #ffffff;
    --gold: #c69c2c;
    --ink: #1c1c1c;
    --black: #000000;
    --shadow: 0 3px 8px rgba(0,0,0,0.28);
  }
  * { margin: 0; padding: 0; box-sizing: border-box; }
  html, body {
    width: 1200px; height: 1001px; overflow: hidden;
    background: var(--backdrop);
    font-family: "Open Sans", Arial, sans-serif;
    color: var(--ink);
  }
  .canvas { position: relative; width: 1200px; height: 1001px; }

  .sheet, .card {
    position: absolute; background: var(--paper);
    box-shadow: var(--shadow); overflow: hidden;
  }
  .wave { position: absolute; left: 0; bottom: 0; width: 100%; display: block; }

  .brand { position: absolute; display: flex; align-items: center; gap: 8px; }
  .brand-dot { border-radius: 50%; background: var(--gold); flex: none; }
  .brand-name { font-weight: 600; color: var(--ink); white-space: nowrap; line-height: 1; }

  /* Letterhead */
  .letterhead { left: 86px; top: 76px; width: 650px; height: 848px; }
  .letterhead .brand { left: 22px; top: 52px; }
  .letterhead .brand-dot { width: 16px; height: 16px; }
  .letterhead .brand-name { font-size: 15px; }
  .letterhead .rule {
    position: absolute; left: 22px; top: 716px; width: 606px; height: 1px; background: var(--gold);
  }
  .contact-list { position: absolute; list-style: none; }
  .contact-list li { display: flex; align-items: center; white-space: nowrap; }
  .contact-list svg { flex: none; fill: none; stroke: var(--gold); stroke-width: 1.6; }
  .letterhead .contact-list { left: 23px; top: 731px; font-size: 13.5px; }
  .letterhead .contact-list li { height: 16.5px; gap: 10px; }
  .letterhead .contact-list svg { width: 9px; height: 9px; }
  .address { position: absolute; text-align: right; white-space: nowrap; }
  .letterhead .address { right: 22px; top: 731px; font-size: 13.5px; line-height: 16px; }

  /* Business cards */
  .card { left: 804px; width: 313px; }
  .card-front { top: 317px; height: 182px; }
  .card-back { top: 545px; height: 180px; }

  .card-front .brand { left: 14px; top: 38px; gap: 5px; }
  .card-front .brand-dot { width: 9px; height: 9px; }
  .card-front .brand-name { font-size: 8.6px; }

  .person { position: absolute; right: 20px; top: 78px; text-align: right; }
  .person-name { font-size: 13px; font-weight: 700; color: var(--gold); line-height: 1; }
  .person-role {
    position: absolute; right: -20px; top: 17px; width: 313px;
    display: flex; align-items: center; gap: 3px;
    font-size: 7.4px; font-weight: 600; white-space: nowrap;
  }
  .person-role::before, .person-role::after { content: ""; height: 1px; background: var(--gold); }
  .person-role::before { flex: 1; }
  .person-role::after { width: 20px; }

  .card-front .contact-list { left: 15px; top: 112px; font-size: 8px; }
  .card-front .contact-list li { height: 10px; gap: 6px; }
  .card-front .contact-list svg { width: 6px; height: 6px; stroke-width: 2; }
  .card-front .address { right: 26px; top: 112px; font-size: 8px; line-height: 10px; }

  .card-back .brand { left: 50%; top: 78px; transform: translateX(-50%); gap: 7px; }
  .card-back .brand-dot { width: 13px; height: 13px; }
  .card-back .brand-name { font-size: 12.5px; }
</style>
</head>
<body>
<main class="canvas">

  <section class="sheet letterhead" aria-label="Letterhead">
    <div class="brand"><span class="brand-dot"></span><span class="brand-name">Fenwell Building Partners</span></div>

    <div class="rule"></div>
    <ul class="contact-list">
      <li><svg viewBox="0 0 10 10"><rect x="2.5" y="0.8" width="5" height="8.4" rx="1"/></svg>+44 (0)7700 900481</li>
      <li><svg viewBox="0 0 10 10"><path d="M1 4 Q5 0 9 4 L8 5 L6.5 4 L3.5 4 L2 5 Z"/><rect x="2.5" y="5" width="5" height="4"/></svg>+44 (0)20 7946 0321</li>
      <li><svg viewBox="0 0 10 10"><path d="M2.5 1 L4.2 3.2 L3.2 4.4 Q4.5 6.5 6 7 L7 6 L9 7.8 L7.8 9 Q3 8.5 1 2.2 Z"/></svg>+44&nbsp; (0)20 7946 0322</li>
      <li><svg viewBox="0 0 10 10"><rect x="0.8" y="2" width="8.4" height="6"/><path d="M0.8 2 L5 5.5 L9.2 2"/></svg>martin.hale@fenwellbp.co.uk</li>
      <li><svg viewBox="0 0 10 10"><circle cx="5" cy="5" r="4.2"/><ellipse cx="5" cy="5" rx="1.8" ry="4.2"/><path d="M0.8 5 H9.2"/></svg>www.fenwellbp.co.uk</li>
    </ul>
    <address class="address" style="font-style:normal">Ardley House,<br>12 Marlow Lane<br>Ashford, Kent, TN23 4QX</address>

    <svg class="wave" viewBox="0 0 650 70" height="70" preserveAspectRatio="none" aria-hidden="true">
      <path d="M0 40 C120 72 260 64 400 40 C520 20 600 16 650 26 L650 70 L0 70 Z" fill="var(--black)"/>
      <path d="M0 30 C120 66 260 58 400 32 C520 12 600 8 650 20" fill="none" stroke="var(--gold)" stroke-width="4"/>
    </svg>
  </section>

  <section class="card card-front" aria-label="Business card, front">
    <div class="brand"><span class="brand-dot"></span><span class="brand-name">Fenwell Building Partners</span></div>

    <div class="person">
      <div class="person-name">Martin Hale</div>
      <div class="person-role">Managing Director</div>
    </div>

    <ul class="contact-list">
      <li><svg viewBox="0 0 10 10"><rect x="2.5" y="0.8" width="5" height="8.4" rx="1"/></svg>+44 (0)7700 900481</li>
      <li><svg viewBox="0 0 10 10"><path d="M1 4 Q5 0 9 4 L8 5 L6.5 4 L3.5 4 L2 5 Z"/><rect x="2.5" y="5" width="5" height="4"/></svg>+44 (0)20 7946 0321</li>
      <li><svg viewBox="0 0 10 10"><path d="M2.5 1 L4.2 3.2 L3.2 4.4 Q4.5 6.5 6 7 L7 6 L9 7.8 L7.8 9 Q3 8.5 1 2.2 Z"/></svg>+44&nbsp; (0)20 7946 0322</li>
      <li><svg viewBox="0 0 10 10"><rect x="0.8" y="2" width="8.4" height="6"/><path d="M0.8 2 L5 5.5 L9.2 2"/></svg>martin.hale@fenwellbp.co.uk</li>
      <li><svg viewBox="0 0 10 10"><circle cx="5" cy="5" r="4.2"/><ellipse cx="5" cy="5" rx="1.8" ry="4.2"/><path d="M0.8 5 H9.2"/></svg>www.fenwellbp.co.uk</li>
    </ul>
    <address class="address" style="font-style:normal">Ardley House,<br>12 Marlow Lane<br>Ashford, Kent, TN23 4QX</address>

    <svg class="wave" viewBox="0 0 313 36" height="36" preserveAspectRatio="none" aria-hidden="true">
      <path d="M0 20 C60 38 130 32 200 18 C250 8 290 6 313 14 L313 36 L0 36 Z" fill="var(--black)"/>
      <path d="M0 14 C60 34 130 28 200 13 C250 3 290 1 313 9" fill="none" stroke="var(--gold)" stroke-width="2.2"/>
    </svg>
  </section>

  <section class="card card-back" aria-label="Business card, back">
    <div class="brand"><span class="brand-dot"></span><span class="brand-name">Fenwell Building Partners</span></div>

    <svg class="wave" viewBox="0 0 313 36" height="36" preserveAspectRatio="none" aria-hidden="true">
      <path d="M0 14 C50 2 110 6 170 20 C230 32 280 30 313 18 L313 36 L0 36 Z" fill="var(--black)"/>
      <path d="M0 9 C50 -2 110 2 170 15 C230 27 280 25 313 12" fill="none" stroke="var(--gold)" stroke-width="2.2"/>
    </svg>
  </section>

</main>
</body>
</html>
```